Quiet Harbor Days Book Cover

I am looking for a front and back cover for my new book, the dimensions are 6 x 9. This book is going to be a normal notepad with bible verses, so I want the cover to be eye-catching, appealing towards women and the title "Quiet Harbor Days" to be big enough that it is easy to read from a thumbnail size. I want the style to be modern, simple and cute with minimal illustrations, maybe just some floral or subtle design. Colors can vary but I prefer them more soft than harsh.
DO NOT INCLUDE SPINE OR AUTHOR NAME ON FRONT COVER. Please include BOTH FRONT & BACK with your submissions.
IF you come across any questions, please let me know - I will try to give detailed feedback.

```html
<!DOCTYPE html>
<html lang="en">
<head>
<meta charset="utf-8">
<title>Quiet Harbor Days – Front and Back Cover</title>
<link rel="stylesheet" href="https://fonts.googleapis.com/css2?family=Dancing+Script:wght@600&display=swap">
<style>
  :root {
    --backdrop: #d9595a;
    --paper: #fbf8d6;
    --paper-edge: #efe9bd;
    --plum: #7b1f5a;
    --rose: #ec7c8c;
    --coral: #f0806a;
    --violet: #a34aa6;
    --peach: #f5a77e;
    --blush: #f5bcd0;
    --lilac: #d9a9e0;
    --leaf: #4f9a55;
    --lime: #c6d865;
  }
  * { box-sizing: border-box; margin: 0; padding: 0; }
  html, body {
    width: 1200px;
    height: 800px;
    overflow: hidden;
    background: var(--backdrop);
  }
  .spread {
    position: absolute;
    top: 90px;
    left: 157px;
    display: flex;
    gap: 60px;
  }
  .cover {
    position: relative;
    width: 413px;
    height: 620px;
    background: var(--paper);
    box-shadow: inset 0 0 0 1px var(--paper-edge), 0 6px 18px rgba(90, 20, 30, 0.25);
    overflow: hidden;
  }
  .floral-band {
    position: absolute;
    left: 0;
    right: 0;
  }
  .floral-band--top {
    top: 0;
    height: 92px;
    background: linear-gradient(90deg,
      var(--leaf) 0%, var(--coral) 6%, var(--rose) 16%, var(--violet) 30%,
      var(--violet) 42%, var(--coral) 56%, var(--peach) 66%, var(--blush) 78%,
      var(--lime) 88%, var(--leaf) 100%);
    -webkit-mask-image: linear-gradient(to bottom, #000 62%, transparent 100%);
    mask-image: linear-gradient(to bottom, #000 62%, transparent 100%);
  }
  .floral-band--bottom {
    bottom: 0;
    height: 128px;
    background: linear-gradient(90deg,
      var(--blush) 0%, var(--peach) 10%, var(--lilac) 18%, var(--violet) 30%,
      var(--violet) 44%, var(--rose) 54%, var(--peach) 64%, var(--blush) 76%,
      var(--rose) 86%, var(--blush) 100%);
    -webkit-mask-image: linear-gradient(to top, #000 58%, transparent 100%);
    mask-image: linear-gradient(to top, #000 58%, transparent 100%);
  }
  .cover--back .floral-band--top { height: 82px; }
  .cover--back .floral-band--bottom {
    height: 100px;
    background: linear-gradient(90deg,
      var(--peach) 0%, var(--rose) 12%, var(--blush) 26%, var(--violet) 40%,
      var(--blush) 54%, var(--rose) 66%, var(--blush) 80%, var(--lilac) 100%);
  }
  .title {
    position: absolute;
    top: 78px;
    left: 30px;
    right: 22px;
    font-family: "Dancing Script", cursive;
    color: var(--plum);
    font-weight: 600;
    line-height: 1;
    white-space: nowrap;
  }
  .title-line { display: block; }
  .title-line--lead { font-size: 150px; }
  .title-line--middle {
    font-size: 74px;
    text-align: right;
    margin-top: -14px;
    padding-right: 6px;
  }
  .title-line--close {
    font-size: 150px;
    margin-top: -22px;
    padding-left: 34px;
  }
</style>
</head>
<body>
  <main class="spread">
    <section class="cover cover--front" aria-label="Front cover">
      <div class="floral-band floral-band--top" role="img" aria-label="Watercolor roses in pink, purple and peach with green leaves along the top edge"></div>
      <h1 class="title">
        <span class="title-line title-line--lead">Quiet</span>
        <span class="title-line title-line--middle">Harbor</span>
        <span class="title-line title-line--close">Days</span>
      </h1>
      <div class="floral-band floral-band--bottom" role="img" aria-label="Watercolor roses in pink, purple and peach with green leaves along the bottom edge"></div>
    </section>
    <section class="cover cover--back" aria-label="Back cover">
      <div class="floral-band floral-band--top" role="img" aria-label="Watercolor roses in pink and purple with green leaves along the top edge"></div>
      <div class="floral-band floral-band--bottom" role="img" aria-label="Watercolor roses in soft pink and purple with green leaves along the bottom edge"></div>
    </section>
  </main>
</body>
</html>
```